Design and Renovation Company Luxury Business Card

I want to create a luxury business card for a Design and Renovation Firm . We will use our current logo. The company name is 742BUILD. We do not want anything standard. We need a very unique concept.
Please see uploaded inspiration. I really like the textured paper option. I would like the card to be thick with debossing, and/or embossing options. The logo has orange in it but I would like to see the card with and without the orange. I think the orange may make the company feel less high-end. The goal is to elevate the logo not match its vibe per se of the logo. We want something very unique, not standard at all!
I would like a space for :
Logo,
Name,
Position,
Email,
Office number,
Website Address,
Business Address,
Thank you!
Have fun!
Target Market(s)
Home owners Age 35 +
Industry/Entity Type
Design and Renovation
Contact Information for Business Card
Logo, Name, Position, Email, Office number, Website Address, Business Address,.
Colors
Designer to choose colors to be used in the design.
Requirements
Must have
- A luxury designer feel. Must be black or dark grey but open to other luxury ideas.
Nice to have
- Gold, silver, black embossing or debossing. Textured paper design.
Should not have
- A cheap look and feel.

```html
<!DOCTYPE html>
<html lang="en">
<head>
<meta charset="utf-8">
<title>742BUILD Business Card</title>
<link rel="stylesheet" href="https://fonts.googleapis.com/css2?family=Questrial&family=Urbanist:wght@700&display=swap">
<style>
  :root {
    --backdrop: #cdcdcd;
    --card-dark: #1f1e1f;
    --card-mid: #2b2a2b;
    --gold: #dbb86f;
    --glyph: #232223;
  }
  * { margin: 0; padding: 0; box-sizing: border-box; }
  html, body {
    width: 1200px; height: 1200px; overflow: hidden;
    background: var(--backdrop);
  }
  .sheet { position: relative; width: 1200px; height: 1200px; }
  .card {
    position: absolute; left: 275px; width: 649px; height: 371px;
    overflow: hidden;
    box-shadow: 14px 16px 22px rgba(0,0,0,0.28);
    color: var(--gold);
  }
  .card--front { top: 154px; }
  .card--back { top: 673px; }
  .card__texture {
    position: absolute; inset: 0;
    background: linear-gradient(135deg, var(--card-dark) 0%, var(--card-mid) 45%, var(--card-dark) 70%, var(--card-mid) 100%);
  }
  .brand-name {
    position: absolute;
    font-family: "Questrial", sans-serif; font-weight: 400;
    color: var(--gold); white-space: nowrap; line-height: 1;
  }

  .card--front .brand-name {
    left: 0; right: 0; top: 160px; text-align: center;
    font-size: 46px; letter-spacing: 6px;
  }
  .tagline {
    position: absolute; left: 0; right: 0; top: 220px; text-align: center;
    font-family: "Questrial", sans-serif;
    font-size: 12px; letter-spacing: 2.6px; white-space: nowrap;
  }
  .website {
    position: absolute; left: 424px; top: 315px;
    font-family: "Questrial", sans-serif; font-size: 15.5px; letter-spacing: 0.4px;
  }

  .card--back .brand-name { left: 100px; top: 283px; font-size: 22px; letter-spacing: 2px; }
  .holder { position: absolute; left: 385px; top: 44px; }
  .holder__name {
    font-family: "Urbanist", sans-serif; font-weight: 700;
    font-size: 33px; letter-spacing: 3.2px; line-height: 1;
    padding-bottom: 4px; border-bottom: 1.5px solid var(--gold);
    width: 210px; white-space: nowrap;
  }
  .holder__title {
    margin-top: 6px;
    font-family: "Urbanist", sans-serif; font-weight: 700; font-size: 13px;
  }
  .contacts { position: absolute; left: 384px; top: 170px; list-style: none; }
  .contacts li {
    display: flex; align-items: flex-start; height: 28.5px;
    font-family: "Questrial", sans-serif; font-size: 16px; letter-spacing: 1.6px; line-height: 18px;
  }
  .contacts li.contacts__address { height: auto; }
  .contacts svg { width: 22px; height: 22px; flex: none; margin-right: 14px; }
</style>
</head>
<body>
<div class="sheet">

  <section class="card card--front">
    <div class="card__texture" role="img" aria-label="Fine diagonal pinstripe texture in charcoal tones"></div>
    <div class="brand-name">742BUILD</div>
    <div class="tagline">Design and Renovation Firm</div>
    <div class="website">www.yourwebsite.com</div>
  </section>

  <section class="card card--back">
    <div class="card__texture" role="img" aria-label="Fine diagonal pinstripe texture in charcoal tones"></div>
    <div class="brand-name">742BUILD</div>

    <div class="holder">
      <div class="holder__name">Your Name</div>
      <div class="holder__title">Your Title</div>
    </div>

    <ul class="contacts">
      <li>
        <svg viewBox="0 0 22 22" aria-hidden="true"><circle cx="11" cy="11" r="11" fill="var(--gold)"/><path d="M7 6.2l2 -.4 1.2 2.6-1.2 1c.6 1.4 1.6 2.4 3 3l1-1.2 2.6 1.2-.4 2c-4.6.2-8.4-3.6-8.2-8.2z" fill="var(--glyph)"/></svg>
        Your Phone Number
      </li>
      <li>
        <svg viewBox="0 0 22 22" aria-hidden="true"><circle cx="11" cy="11" r="11" fill="var(--gold)"/><g fill="none" stroke="var(--glyph)" stroke-width="1"><circle cx="11" cy="11" r="5.5"/><ellipse cx="11" cy="11" rx="2.4" ry="5.5"/><path d="M5.5 11h11M6.4 8h9.2M6.4 14h9.2"/></g></svg>
        Your Email Address
      </li>
      <li>
        <svg viewBox="0 0 22 22" aria-hidden="true"><circle cx="11" cy="11" r="11" fill="var(--gold)"/><g fill="none" stroke="var(--glyph)" stroke-width="1.1"><rect x="5.5" y="7.5" width="11" height="7.5"/><path d="M5.5 7.5l5.5 4.5 5.5-4.5M5.5 15l4-3.5M16.5 15l-4-3.5"/></g></svg>
        Your Site Here
      </li>
      <li class="contacts__address">
        <svg viewBox="0 0 22 22" aria-hidden="true"><circle cx="11" cy="11" r="11" fill="var(--gold)"/><path d="M11 4.5a4.5 4.5 0 0 0-4.5 4.5c0 3.4 4.5 8.5 4.5 8.5s4.5-5.1 4.5-8.5A4.5 4.5 0 0 0 11 4.5z" fill="var(--glyph)"/><circle cx="11" cy="9" r="1.6" fill="var(--gold)"/></svg>
        <span>Your Address Here<br>Your Street Name<br>Your Country</span>
      </li>
    </ul>
  </section>

</div>
</body>
</html>
```